Web Banner for Local classified site

Have sent a sketch mock up of type of layout wanted. Please contact if more information needed.
This is for a website design header / layout / logo for local classified site called Swap Down the Lane.
Concept that design must convey.
Buying and selling local
We are looking for something with the colour scheme blue / white (blue along the lines of Chatterbox blue)
Simple clean line design
We like the idea of using stick men / women as neighbours exchanging money over a fence as in sketch.
The items listed for sale on the sketch should be represented as images / icons and not limited to items shown on the sketch.
The final design should communicate the ease and simplicity of buying or selling to your local neighbour.
Updates
This image is for the BANNER / HEADER of a website NOT a logo. Please use the ideas presented in the sketch we provided.
Reason: The banner i like the most is the one entered by PixelRook. However i would like a few changes. I want the word ''Whos'' taken out, The people exchanging money must be stick men and the items for sale must be animated or sketched (not photos). A few more items would be good. I like the bright colors.
Thanks for all the designs so far, for me this one stands out the most.
Gordon
Reason: Designer is making a few changes
Industry/Entity Type
Fence
Logo Text
Who's Swapping Down the Lane...
Look and feel
Each slider illustrates characteristics of the customer's brand and the style your logo design should communicate.

```html
<!DOCTYPE html>
<html lang="en">
<head>
<meta charset="utf-8">
<title>Swap Down the Lane – Header</title>
<link rel="stylesheet" href="https://fonts.googleapis.com/css2?family=Delius&display=swap">
<style>
  :root {
    --lane-blue: #0f5d9d;
    --lane-sky: #5a8fbf;
    --lane-white: #ffffff;
  }
  html, body {
    margin: 0;
    padding: 0;
    overflow: hidden;
    background: var(--lane-blue);
  }
  .banner {
    position: relative;
    width: 1200px;
    height: 239px;
    background: var(--lane-blue);
    overflow: hidden;
  }
  .banner__curves {
    position: absolute;
    inset: 0;
    width: 1200px;
    height: 239px;
  }
  .curve-fill { fill: var(--lane-sky); }
  .curve-band {
    fill: none;
    stroke: var(--lane-blue);
    stroke-width: 14;
  }
  .brand {
    position: absolute;
    left: 700px;
    top: 82px;
    display: flex;
    align-items: center;
    gap: 18px;
    color: var(--lane-white);
    font-family: "Delius", sans-serif;
    font-weight: 400;
  }
  .brand__dot {
    width: 44px;
    height: 44px;
    border-radius: 50%;
    background: var(--lane-white);
    flex: none;
  }
  .brand__name {
    margin: 0;
    font-size: 38px;
    line-height: 1;
    font-weight: 400;
  }
  .brand__name-sub {
    display: block;
    font-size: 26px;
    margin-top: 4px;
  }
</style>
</head>
<body>
  <header class="banner">
    <svg class="banner__curves" viewBox="0 0 1024 204" preserveAspectRatio="none" aria-hidden="true">
      <path class="curve-fill" d="M0,0 H158 Q222,95 236,204 H0 Z"/>
      <path class="curve-band" d="M62,-4 Q170,90 190,210"/>
      <path class="curve-band" d="M-4,108 Q90,112 118,210"/>
      <path class="curve-fill" d="M904,0 H1024 V162 Q985,118 955,72 Q925,28 904,0 Z"/>
    </svg>
    <div class="brand">
      <span class="brand__dot"></span>
      <h1 class="brand__name">who’s swapping<span class="brand__name-sub">Down the Lane</span></h1>
    </div>
  </header>
</body>
</html>
```